Modern Spot UV Business Card design

We are a relatively new real estate agency. We need a business card that reflects the professionalism and prestige of our company but is also modern and fresh, based around our logo.
We would love to utilise spot UV.
Happy to let the designers use their imagination and see what they come up with (we're not very creative, so have no ideas for you, sorry) :-)
We'd like one for each staff member, but I've just provided one staff members photo here to avoid confusion.

Target Market(s)

Families

Industry/Entity Type

Real Estate Agent

Contact Information for Business Card

Colin Varga - Director & Principal
Mobile: 0491 527 806
Email: colin.varga@vbrokers.example.com.au
Phone: (08) 7364 9150
Fax: (08) 7364 9182
www.vargabrokersrealestate.example.com.au

Font styles to use
Other font styles liked:
• Kabel Dm BT

Requirements
Must have
• Contact details, logo, photo, spot UV
Nice to have
• Modern interesting features that will make people comment. Nothing too feminine nor too masculine.
Should not have
• No houses! Nothing typical of a real estate agent.

```html
<!DOCTYPE html>
<html lang="en">
<head>
<meta charset="utf-8">
<title>Colin Varga – Business Card</title>
<link rel="stylesheet" href="https://fonts.googleapis.com/css2?family=Arimo:wght@400;700&display=swap">
<style>
  :root {
    --sky: #00c6f8;
    --orange: #ff7f00;
    --ink: #111111;
    --icon-blue: #4b9fd2;
    --icon-cyan: #4fd3ee;
    --frame-dark: #6f7479;
    --frame-light: #e9ecef;
    --ghost: #e4e4e4;
    --paper: #ffffff;
  }
  * { box-sizing: border-box; margin: 0; padding: 0; }
  html, body { width: 1200px; height: 582px; overflow: hidden; background: var(--paper); }
  body { font-family: "Arimo", Arial, sans-serif; color: var(--ink); }

  .card { position: relative; width: 1200px; height: 582px; overflow: hidden; background: var(--paper); }

  .top-band { position: absolute; top: 0; left: 0; width: 1200px; height: 51px; display: flex; }
  .top-band .band-blue { width: 602px; background: var(--sky); }
  .top-band .band-orange { flex: 1; background: var(--orange); }

  .chevrons { position: absolute; left: 0; top: 80px; }

  .brand-ghost {
    position: absolute; left: 698px; top: 330px; z-index: 0;
    color: var(--ghost); font-weight: 400; font-size: 36px; line-height: 1;
    letter-spacing: 1px; white-space: nowrap;
  }

  .portrait-frame {
    position: absolute; left: 66px; top: 124px; width: 265px; height: 323px;
    background: linear-gradient(90deg, var(--frame-light) 0%, var(--frame-dark) 100%);
  }
  .portrait {
    position: absolute; left: 12px; top: 18px; width: 240px; height: 285px;
    background: linear-gradient(180deg, #f4f4f4 0%, #cfd3d8 45%, #3d4550 100%);
  }

  .person { position: absolute; left: 66px; top: 466px; width: 290px; text-align: center; }
  .person .name { font-size: 45px; font-weight: 400; line-height: 1; }
  .person .role { font-size: 22px; margin-top: 8px; }

  .contact-row { position: absolute; left: 556px; z-index: 1; display: flex; align-items: center; gap: 70px; }
  .contact-row .label { font-size: 36px; white-space: nowrap; }
  .row-mobile { top: 125px; }
  .row-phone { top: 250px; }
  .row-fax { top: 375px; }

  .email-bar {
    position: absolute; left: 464px; top: 510px; width: 736px; height: 68px;
    background: var(--orange); display: flex; align-items: center; padding-left: 10px; gap: 10px;
  }
  .email-bar .label { color: var(--paper); font-size: 27px; white-space: nowrap; }
</style>
</head>
<body>
<div class="card">
  <div class="top-band"><div class="band-blue"></div><div class="band-orange"></div></div>

  <svg class="chevrons" width="330" height="440" viewBox="0 0 330 440" aria-hidden="true">
    <polyline points="10,110 80,20 200,160" fill="none" stroke="#fde3cc" stroke-width="34"/>
    <polyline points="0,210 90,120 240,270" fill="none" stroke="#fbd7b8" stroke-width="30"/>
    <polyline points="0,290 80,360 280,180" fill="none" stroke="#cdeefb" stroke-width="36"/>
  </svg>

  <div class="brand-ghost">Varga Brokers Real Estate</div>

  <div class="portrait-frame">
    <div class="portrait" role="img" aria-label="Portrait photo of Colin Varga"></div>
  </div>

  <div class="person">
    <div class="name">Colin Varga</div>
    <div class="role">Director &amp; Principal</div>
  </div>

  <div class="contact-row row-mobile">
    <svg width="72" height="72" viewBox="0 0 72 72" aria-hidden="true">
      <circle cx="36" cy="36" r="35" fill="var(--icon-blue)"/>
      <rect x="25" y="14" width="22" height="42" rx="3" fill="#fff"/>
      <rect x="28" y="19" width="16" height="29" fill="#8cc6ea"/>
      <circle cx="36" cy="52" r="2" fill="var(--icon-blue)"/>
    </svg>
    <span class="label">Mobile: 0491 527 806</span>
  </div>

  <div class="contact-row row-phone">
    <svg width="72" height="72" viewBox="0 0 72 72" aria-hidden="true">
      <circle cx="36" cy="36" r="33" fill="#fff" stroke="var(--icon-cyan)" stroke-width="4"/>
      <path d="M18 36 L36 20 L54 36 L49 36 L49 54 L23 54 L23 36 Z" fill="var(--icon-cyan)"/>
      <rect x="32" y="42" width="8" height="12" fill="#fff"/>
    </svg>
    <span class="label">Phone: (08) 7364 9150</span>
  </div>

  <div class="contact-row row-fax">
    <svg width="72" height="72" viewBox="0 0 72 72" aria-hidden="true">
      <circle cx="36" cy="36" r="35" fill="var(--icon-blue)"/>
      <rect x="24" y="14" width="24" height="14" fill="#fff"/>
      <rect x="14" y="26" width="44" height="22" rx="3" fill="#fff"/>
      <rect x="24" y="40" width="24" height="18" fill="#e8f4fb" stroke="var(--icon-blue)" stroke-width="2"/>
      <circle cx="30" cy="34" r="3" fill="var(--icon-blue)"/>
    </svg>
    <span class="label">Fax: (08) 7364 9182</span>
  </div>

  <div class="email-bar">
    <svg width="70" height="52" viewBox="0 0 70 52" aria-hidden="true">
      <rect x="1" y="1" width="68" height="50" fill="#f4f4f4" stroke="#2f5fb0" stroke-width="2"/>
      <polyline points="3,4 35,30 67,4" fill="none" stroke="#2f5fb0" stroke-width="6"/>
      <rect x="1" y="1" width="6" height="50" fill="#2f5fb0"/>
      <rect x="63" y="1" width="6" height="50" fill="#2f5fb0"/>
    </svg>
    <span class="label">Email: colin.varga@vbrokers.example.com.au</span>
  </div>
</div>
</body>
</html>
```